businesscard, flyer and membercard

--------------------------------------------------------------------------------------------------
design flyer :
- delivering format (jpg, pdf and original psd)
- there is a example how the flyers should look like
the text and logo should be the same as the exemple flyer, the creativity is yours.
- the design should have a back and front side.
File format : 15,0 cm x 21,2 cm
design membercard :
- there is example how the member-card should look like
the text and logo should be the same as the exemple membercard, the creativity is yours.
- the front side contains text and open space where for writing :
Naam ......
Dansstijlen ......
- the front side contains 12 circels horizontal at the line name at the end of the line "Salsa".
- the front side contains 12 circels horizontal at the line name at the end of the line "Bachata".
- the front side contains 12 circels horizontal at the line name at the end of the line "Kizomba".
- each horizontal line with circels contains a different kind of color/design.
- file format: 7,6 cm x 10,7 cm
Business card :
- there is example how the businesscard should look like
the text and logo should be the same as the exemple buisinesscard, the creativity is yours.
- the design should have a back a front side
File format : 8,7 cm x 5,7 cm

Target Market(s)

Dancing :Salsa, Bachata and Kizomba

Colors

Designer to choose colors to be used in the design.

Requirements
Must have
• same text as seen on the examples.
Nice to have
• see the examples as attachments
Should not have
• - REMOVE TEXT "KOV" from the design
• - REMOVE TEXT "Gratis Parkeren"

```html
<!DOCTYPE html>
<html lang="nl">
<head>
<meta charset="utf-8">
<title>Nexa Dance Studio – Lid Kaart</title>
<link rel="stylesheet" href="https://fonts.googleapis.com/css2?family=Lato:wght@400;700&family=Raleway:wght@300;600&family=Roboto+Condensed:ital,wght@0,400;1,700&family=Oswald:wght@600&family=Gochi+Hand&display=swap">
<style>
:root{
  --board-light:#f2f2f2;
  --board-dark:#d9d9d9;
  --ink:#111;
  --accent-red:#e8141c;
  --card-top:#4a2c5e;
  --card-mid:#8a2a63;
  --card-low:#c4285e;
  --card-bottom:#d8336a;
  --band:#7a1b4a;
  --white:#fff;
  --stamp-ink:#3a3a3a;
  --stamp-ring:#8c1240;
  --title-pink:#f6b3d6;
  --label-navy:#1d1760;
}
*{box-sizing:border-box;margin:0;padding:0}
html,body{width:1200px;height:902px;overflow:hidden}
body{
  background:radial-gradient(ellipse at 50% 40%,var(--board-light) 0%,var(--board-dark) 100%);
  position:relative;font-family:"Lato",sans-serif;
}
.board-title{
  position:absolute;top:40px;left:0;width:1200px;text-align:center;
  font-family:"Lato",sans-serif;font-size:33px;letter-spacing:4px;color:var(--ink);line-height:40px;
}
.board-title strong{font-weight:700}
.board-title .light{font-weight:400}
.board-note{
  position:absolute;top:80px;left:0;width:1200px;text-align:center;
  font-size:33px;letter-spacing:4px;color:var(--accent-red);
}
.card{
  position:absolute;top:250px;width:403px;height:565px;overflow:hidden;
  box-shadow:0 4px 10px rgba(0,0,0,.35);color:var(--white);
}
.card--front{left:161px}
.card--back{left:629px}
.card-photo{
  position:absolute;inset:0;
  background:
    radial-gradient(circle at 20% 25%,rgba(30,20,40,.7) 0%,transparent 40%),
    radial-gradient(circle at 75% 40%,rgba(200,60,80,.45) 0%,transparent 35%),
    linear-gradient(180deg,var(--card-top) 0%,var(--card-mid) 45%,var(--card-low) 75%,var(--card-bottom) 100%);
}
.brand{
  position:absolute;left:0;width:100%;text-align:center;
  font-family:"Raleway",sans-serif;font-weight:600;color:var(--white);letter-spacing:3px;
}
.card--front .brand{top:38px;font-size:24px;line-height:30px}
.card--back .brand{top:100px;font-size:30px;line-height:38px}
.brand small{display:block;font-size:.6em;letter-spacing:1px}
.card-heading{
  position:absolute;left:0;width:100%;text-align:center;
  font-family:"Raleway",sans-serif;font-weight:300;letter-spacing:3px;
}
.card--front .card-heading{top:160px;font-size:30px}
.card--back .card-heading{top:228px;font-size:22px}
.form-row{position:absolute;left:0;display:flex;align-items:center;height:24px}
.form-row label{
  width:116px;padding-right:4px;text-align:right;
  font-family:"Roboto Condensed",sans-serif;font-style:italic;font-weight:700;font-size:18px;color:var(--white);
}
.form-row .field{width:251px;height:22px;background:var(--white);border:1px solid #ddd}
.form-row--name{top:248px}
.form-row--styles{top:274px}
.stamps{position:absolute;left:16px;display:flex;gap:7px}
.stamps--one{top:347px}
.stamps--two{top:406px}
.stamp{
  width:47px;height:47px;border-radius:50%;background:var(--white);border:2px solid var(--stamp-ring);
  display:flex;align-items:center;justify-content:center;
  font-family:"Gochi Hand",cursive;font-size:36px;color:var(--stamp-ink);line-height:1;
}
.address{
  position:absolute;top:490px;left:0;width:100%;text-align:center;
  font-family:"Roboto Condensed",sans-serif;font-size:17px;
}
.contact-band{
  position:absolute;top:523px;left:0;width:100%;height:26px;background:var(--band);
  display:flex;justify-content:space-between;align-items:center;padding:0 34px 0 36px;
  font-family:"Roboto Condensed",sans-serif;font-size:12px;
}
.contact-item{display:flex;align-items:center;gap:5px}
.contact-item svg{width:14px;height:14px}
.program-title{
  position:absolute;top:292px;left:0;width:100%;text-align:center;
  font-family:"Oswald",sans-serif;font-weight:600;font-size:44px;line-height:42px;
  color:var(--title-pink);text-shadow:0 0 6px rgba(255,255,255,.5);letter-spacing:-.5px;
}
.progress-row{position:absolute;left:0;display:flex;align-items:center;height:26px}
.progress-row .style-name{
  width:118px;padding-right:10px;text-align:right;
  font-family:"Roboto Condensed",sans-serif;font-size:26px;color:var(--white);
}
.progress-row--salsa{top:374px}
.progress-row--bachata{top:420px}
.progress-row--kizomba{top:467px}
.dots{display:flex;gap:1px}
.dot{width:22px;height:22px;border-radius:50%;border:1.5px solid rgba(255,255,255,.85)}
.dot:nth-child(1){background:#f4e41c}
.dot:nth-child(2){background:#f7b217}
.dot:nth-child(3){background:#f38b1d}
.dot:nth-child(4){background:#ee5b2a}
.dot:nth-child(5){background:#e3212c}
.dot:nth-child(6){background:#c0207a}
.dot:nth-child(7){background:#7d2a90}
.dot:nth-child(8){background:#4b3c9b}
.dot:nth-child(9){background:#1f78c7}
.dot:nth-child(10){background:#13a3a0}
.dot:nth-child(11){background:#3cb54a}
.dot:nth-child(12){background:#a6cf38}
</style>
</head>
<body>
<div class="board-title"><strong>MEMBER CARD</strong> <span class="light">&nbsp;(FRONT &amp; BACK)</span></div>
<div class="board-note">[REVISED]</div>

<section class="card card--front">
  <div class="card-photo" role="img" aria-label="Photograph of a ballroom dancing couple against a purple and pink stage glow"></div>
  <div class="brand">NEXA<small>DANCE STUDIO</small></div>
  <div class="card-heading">LID KAART</div>
  <div class="form-row form-row--name"><label>Naam:</label><div class="field"></div></div>
  <div class="form-row form-row--styles"><label>Dansstijlen:</label><div class="field"></div></div>
  <div class="stamps stamps--one">
    <div class="stamp">1</div><div class="stamp">2</div><div class="stamp">3</div><div class="stamp">4</div><div class="stamp">5</div><div class="stamp">6</div><div class="stamp">7</div>
  </div>
  <div class="stamps stamps--two">
    <div class="stamp">1</div><div class="stamp">2</div><div class="stamp">3</div><div class="stamp">4</div><div class="stamp">5</div><div class="stamp">6</div><div class="stamp">7</div>
  </div>
  <div class="address">Dorpsweg 14, 2500 AB Den Haag</div>
  <div class="contact-band">
    <span class="contact-item"><svg viewBox="0 0 14 14"><circle cx="7" cy="7" r="6" fill="none" stroke="#fff"/><path d="M4.5 4l1.5-.5 1 2-1 .8a4 4 0 0 0 1.7 1.7l.8-1 2 1-.5 1.5c-3 0-5.5-2.5-5.5-5.5z" fill="#fff"/></svg>0612345678</span>
    <span class="contact-item"><svg viewBox="0 0 14 14"><circle cx="7" cy="7" r="6" fill="none" stroke="#fff"/><rect x="4" y="5" width="6" height="4" fill="none" stroke="#fff" stroke-width=".8"/><path d="M4 5l3 2.2L10 5" fill="none" stroke="#fff" stroke-width=".8"/></svg>info@nexadans.nl</span>
    <span class="contact-item"><svg viewBox="0 0 14 14"><circle cx="7" cy="7" r="6" fill="none" stroke="#fff"/></svg>Nexadenhaag</span>
  </div>
</section>

<section class="card card--back">
  <div class="card-photo" role="img" aria-label="Photograph of a ballroom dancing couple with sparkling pink bokeh lights"></div>
  <div class="brand">NEXA<small>DANCE STUDIO</small></div>
  <div class="card-heading">LID KAART</div>
  <div class="program-title">SALSA-BACHATA&amp;<br>KIZOMBA</div>
  <div class="progress-row progress-row--salsa"><span class="style-name">SALSA</span>
    <div class="dots"><i class="dot"></i><i class="dot"></i><i class="dot"></i><i class="dot"></i><i class="dot"></i><i class="dot"></i><i class="dot"></i><i class="dot"></i><i class="dot"></i><i class="dot"></i><i class="dot"></i><i class="dot"></i></div></div>
  <div class="progress-row progress-row--bachata"><span class="style-name">BACHATA</span>
    <div class="dots"><i class="dot"></i><i class="dot"></i><i class="dot"></i><i class="dot"></i><i class="dot"></i><i class="dot"></i><i class="dot"></i><i class="dot"></i><i class="dot"></i><i class="dot"></i><i class="dot"></i><i class="dot"></i></div></div>
  <div class="progress-row progress-row--kizomba"><span class="style-name">KIZOMA</span>
    <div class="dots"><i class="dot"></i><i class="dot"></i><i class="dot"></i><i class="dot"></i><i class="dot"></i><i class="dot"></i><i class="dot"></i><i class="dot"></i><i class="dot"></i><i class="dot"></i><i class="dot"></i><i class="dot"></i></div></div>
  <div class="contact-band">
    <span class="contact-item"><svg viewBox="0 0 14 14"><circle cx="7" cy="7" r="6" fill="none" stroke="#fff"/><path d="M4.5 4l1.5-.5 1 2-1 .8a4 4 0 0 0 1.7 1.7l.8-1 2 1-.5 1.5c-3 0-5.5-2.5-5.5-5.5z" fill="#fff"/></svg>0612345678</span>
    <span class="contact-item"><svg viewBox="0 0 14 14"><circle cx="7" cy="7" r="6" fill="none" stroke="#fff"/><rect x="4" y="5" width="6" height="4" fill="none" stroke="#fff" stroke-width=".8"/><path d="M4 5l3 2.2L10 5" fill="none" stroke="#fff" stroke-width=".8"/></svg>info@nexadans.nl</span>
    <span class="contact-item"><svg viewBox="0 0 14 14"><circle cx="7" cy="7" r="6" fill="none" stroke="#fff"/></svg>Nexadenhaag</span>
  </div>
</section>
</body>
</html>
```